Atelier Marrow Architecture business card

We need to update our business card. We do high end custom residential, hospitality, and wellness architecture. We focus on creating unique spaces and design around the five senses, believing that architecture's true impact is not on our surroundings, but within us. We would like to see designs are instill a sense of calm awe. They should be crisp, fresh, clean, authentic, & contemporary without being sterile, overworked, or harsh. White space is important. Alternative materials are an option if natural. We have created our own logo and would like designs to incorporate it. However, we are willing to see alternatives if the logo becomes a stumbling block and you have an alternate you suggest. Card must have the following information:
Atelier Marrow Architecture, Inc.
728 Holloway Ct. NE Atlanta, GA 30318
Marcus T. Whitcombe, AIA, NCARB, LEED AP BD+C
ateliermarrow.example

Target Market(s)

Higher net worth individuals with an appreciation for design, nature, sustainability,

Industry/Entity Type

Architect

Contact Information for Business Card

See above. The title of Owner or Architect is helpful but not necessary. Minimalism should trump additional information.

Font styles to use
Serif
Sans Serif

Requirements
Must have
• It should look professional. It must use logo
Should not have
• caligraphy, animals, anything that is cute,

```html
<!DOCTYPE html>
<html lang="en">
<head>
<meta charset="utf-8">
<title>Atelier Marrow Architecture – Business Card</title>
<link rel="stylesheet" href="https://fonts.googleapis.com/css2?family=Open+Sans:wght@400;500&display=swap">
<style>
  :root {
    --backdrop: #e9e8e4;
    --card-white: #ffffff;
    --forest: #067816;
    --ink: #111111;
    --wordmark: #3a3a3a;
    --on-forest: #ffffff;
  }
  * { box-sizing: border-box; margin: 0; padding: 0; }
  html, body {
    width: 1200px; height: 900px; overflow: hidden;
    background: var(--backdrop);
    font-family: "Open Sans", Arial, sans-serif;
  }
  .card {
    position: absolute; left: 111px; top: 148px;
    width: 978px; height: 605px;
    background: var(--card-white);
    box-shadow: 0 10px 30px rgba(0,0,0,0.15);
    overflow: hidden;
  }
  .card__wave { position: absolute; inset: 0; width: 100%; height: 100%; }
  .brand {
    position: absolute; left: 66px; top: 118px;
    display: flex; align-items: center; gap: 20px;
  }
  .brand__mark { width: 34px; height: 34px; background: var(--forest); }
  .brand__name {
    color: var(--wordmark); font-weight: 400;
    font-size: 30px; letter-spacing: 0.16em; text-transform: uppercase; line-height: 1.2;
  }
  .brand__name small {
    display: block; font-size: 15px; letter-spacing: 0.62em;
  }
  .details {
    position: absolute; right: 40px; top: 290px;
    text-align: right; color: var(--on-forest);
  }
  .details__name {
    font-size: 31px; font-weight: 400; font-variant: small-caps; letter-spacing: 0.02em; line-height: 1.2;
  }
  .details__credentials { font-size: 23px; margin-top: 4px; }
  .contact { list-style: none; margin-top: 26px; font-size: 23px; line-height: 35px; }
  .contact li { display: flex; justify-content: flex-end; align-items: center; gap: 9px; }
  .contact svg { width: 17px; height: 17px; fill: var(--on-forest); }
  .details__address { font-size: 23px; margin-top: 18px; }
</style>
</head>
<body>
  <article class="card">
    <svg class="card__wave" viewBox="0 0 652 403" preserveAspectRatio="none" aria-hidden="true">
      <path fill="var(--ink)" d="M0,203 C80,282 150,309 220,306 C320,302 420,140 530,113 C590,99 630,118 652,150 L652,403 L0,403 Z"/>
      <path fill="var(--card-white)" d="M0,212 C80,295 150,324 220,322 C320,318 420,152 530,124 C590,110 630,128 652,158 L652,403 L0,403 Z"/>
      <path fill="var(--forest)" d="M0,216 C80,300 150,328 220,327 C320,323 420,160 530,131 C590,117 630,135 652,165 L652,403 L0,403 Z"/>
    </svg>

    <div class="brand">
      <span class="brand__mark"></span>
      <p class="brand__name">Atelier Marrow<small>Architecture</small></p>
    </div>

    <section class="details">
      <h1 class="details__name">Marcus T. Whitcombe</h1>
      <p class="details__credentials">AIA, NCARB, LEED AP BD+C</p>
      <ul class="contact">
        <li>044-555 018 274
          <svg viewBox="0 0 24 24"><path d="M6.6 10.8a15.1 15.1 0 0 0 6.6 6.6l2.2-2.2a1 1 0 0 1 1-.25 11.4 11.4 0 0 0 3.6.57 1 1 0 0 1 1 1V20a1 1 0 0 1-1 1A17 17 0 0 1 3 4a1 1 0 0 1 1-1h3.5a1 1 0 0 1 1 1c0 1.25.2 2.45.57 3.57a1 1 0 0 1-.25 1z"/></svg>
        </li>
        <li>info@ateliermarrow.example
          <svg viewBox="0 0 24 24"><path d="M2 5h20v14H2z M3.5 6.5v.6L12 12.5l8.5-5.4v-.6z" fill-rule="evenodd"/></svg>
        </li>
        <li>www.ateliermarrow.example
          <svg viewBox="0 0 24 24"><path fill="none" stroke="#fff" stroke-width="2" d="M12 3a9 9 0 1 0 0 18a9 9 0 1 0 0-18zM3 12h18M12 3c3 3 3 15 0 18M12 3c-3 3-3 15 0 18"/></svg>
        </li>
      </ul>
      <p class="details__address">728 Holloway Ct. NE Atlanta, GA 30318</p>
    </section>
  </article>
</body>
</html>
```